Crestline Forge Alloys Website

I need a redesign of my current website: www.crestlineforgealloys.example.
I would like to update the look, add some new stock photos of shiny stainless steel bar stock items. All of our grades of material should show on each page so that when people search for the grades on Google, our company site comes up. Most of the text content will be the same with some more changes. Also, we will want to add a button for calling our company for sales calls and one for sending a request for quote. I want the graphics to get prospects attention. I won't people to see us as a large stocking facility that is strong. Bold colors, silver, red, and blue.

Target Market(s)

Contract manufacturers, screw machine houses, medical instrument manufacturers, oil and gas parts industry, aerospace industry, automotive industry, food industry

Number of Pages Required

5+ page

Font styles to use
Sans Serif

Colors
ec1f27
0355a3

Requirements
Must have
• Pictures of stainless steel round bar. Also, a button linking someone to sales@crestlineforgealloys.example and our phone # 555-273-8640. Main stainless steel and titanium grades listed on each and every page. Also, a 1 page copy of our ISO 9001 certificatation.

```html
<!DOCTYPE html>
<html lang="en">
<head>
<meta charset="utf-8">
<title>Crestline Forge Alloys</title>
<link href="https://fonts.googleapis.com/css2?family=Roboto:wght@300;400&family=Open+Sans:wght@400&family=Oswald:wght@400&family=Tinos:ital@0;1&display=swap" rel="stylesheet">
<style>
:root{
  --blue:#0355a3;
  --red:#ec1f27;
  --dark:#2b2b2b;
  --page:#f2f2f2;
  --text:#666;
  --nav-text:#555;
}
*{margin:0;padding:0;box-sizing:border-box}
html,body{width:1200px;height:1116px;overflow:hidden;background:var(--page)}
body{position:relative;font-family:'Open Sans',sans-serif}
.header{position:absolute;left:0;top:0;width:1200px;height:158px;background:var(--blue)}
.brand{position:absolute;left:172px;top:32px;font:400 34px 'Tinos',serif;color:#fff;text-shadow:0 1px 2px rgba(0,0,0,.4)}
.toll{position:absolute;left:673px;top:41px;font:italic 700 21px 'Tinos',serif;color:#fff;text-shadow:0 1px 2px rgba(0,0,0,.4)}
.call-btn{position:absolute;left:938px;top:37px;width:91px;height:34px;background:#fff;border-radius:3px;font:italic 700 20px 'Tinos',serif;color:var(--blue);text-align:center;line-height:34px}
.nav{position:absolute;left:172px;top:105px;width:857px;height:53px;background:#f7f7f7;border-radius:4px 4px 0 0;display:flex;overflow:hidden}
.nav a{font:300 15.5px 'Roboto',sans-serif;color:var(--nav-text);text-decoration:none;line-height:53px;padding:0 17px;border-right:1px solid #e6e6e6}
.nav a.active{background:var(--red);color:#fff;padding:0 25px}
.nav a.first-after{padding-left:25px}
.nav a:last-child{border-right:none}
.slider{position:absolute;left:172px;top:158px;width:857px;height:446px;background:#fff;border:1px solid #e4e4e4;border-top:none}
.slide-photo{position:absolute;left:8px;top:8px;width:840px;height:429px;background:linear-gradient(160deg,#3a3a3e 0%,#9a9ba0 25%,#e0e1e4 40%,#77787d 55%,#c9cacd 70%,#5a5b5f 88%,#8c8d90 100%)}
.caption{position:absolute;left:692px;top:335px;width:329px;height:260px;background:rgba(25,25,25,.88);padding:13px 26px 0 20px;color:#fff}
.caption h2{font:400 36px 'Oswald',sans-serif;letter-spacing:-.5px;line-height:44px}
.caption h3{font:400 22px 'Oswald',sans-serif;margin-top:6px;line-height:30px;letter-spacing:-.3px}
.caption p{font:400 12.2px 'Roboto',sans-serif;line-height:20.5px;margin-top:10px;text-align:justify;padding-left:2px}
.arrow{position:absolute;top:567px;width:29px;height:28px;display:flex;align-items:center;justify-content:center}
.arrow.prev{left:963px;background:var(--red)}
.arrow.next{left:992px;background:#333}
.slider-shadow{position:absolute;left:180px;top:604px;width:840px;height:12px;background:radial-gradient(ellipse at top,rgba(0,0,0,.15),transparent 70%)}
.card{position:absolute;top:640px;width:270px;height:249px;background:#fff;border:1px solid #e6e6e6;padding:0 20px}
.card h2{font:400 20.5px 'Roboto',sans-serif;color:var(--red);margin-top:19px;padding-left:3px}
.card h4{font:400 15px 'Roboto',sans-serif;color:#555;margin-top:14px;padding-left:1px}
.card p{font:400 11.4px 'Open Sans',sans-serif;color:var(--text);line-height:20.5px;margin-top:11px}
.card h4+p{margin-top:10px}
.card .quote{position:relative;padding:0 0 0 22px;text-align:justify;line-height:19.7px;margin-top:14px}
.quote .mark{position:absolute;font:700 30px Georgia,serif;color:#bbb;line-height:1}
.quote .open{left:0;top:-4px}
.quote .close{right:-4px;bottom:-22px}
.read-more{position:absolute;left:20px;top:196px;width:87px;height:31px;background:#f5f5f5;border:1px solid #e2e2e2;border-radius:3px;font:400 12.5px 'Open Sans',sans-serif;color:var(--blue);text-align:center;line-height:29px}
.footer{position:absolute;left:0;top:936px;width:1200px;height:180px;background:var(--dark);color:#fff}
.cert-seal{position:absolute;left:173px;top:17px}
.divider{position:absolute;top:22px;width:1px;height:66px;background:#444}
.footer .info{position:absolute;top:31px;font:400 15.3px 'Open Sans',sans-serif;line-height:26px}
.quote-btn{position:absolute;left:878px;top:35px;width:149px;height:39px;background:var(--blue);border-radius:20px;font:400 17px 'Oswald',sans-serif;text-align:center;line-height:39px}
.rule{position:absolute;left:376px;top:116px;width:653px;height:1px;background:#404040}
.copyright{position:absolute;left:376px;top:139px;font:400 12.3px 'Roboto',sans-serif;color:#ccc}
.social{position:absolute;top:135px;width:27px;height:27px;border:1.5px solid #777;border-radius:50%}
</style>
</head>
<body>
<header class="header">
  <div class="brand">Crestline Forge Alloys</div>
  <div class="toll">Toll Free : + (555)-273-8640</div>
  <div class="call-btn">Call us</div>
  <nav class="nav">
    <a class="active">Home</a>
    <a class="first-after">Products</a>
    <a>Quality</a>
    <a>Locations</a>
    <a>Hard to Find Services</a>
    <a>Large Volume</a>
    <a>Inquiries</a>
    <a>FAQ</a>
  </nav>
</header>

<section class="slider">
  <div class="slide-photo" role="img" aria-label="Stack of polished stainless steel round bar stock"></div>
</section>
<div class="caption">
  <h2>Crestline Forge Alloys</h2>
  <h3>National Distributor Specialist</h3>
  <p>Crestline Forge Alloys is a national distributor specializing in the distribution of stainless steel, titanium, and aluminum bar stock, sheet, plate, pipe, tubing, wire, and coil. We have 7 stocking facilities throughout the country offering 1-2 day delivery on stock items to virtually any area of the U.S.A.</p>
</div>
<div class="arrow prev"><svg width="8" height="12" viewBox="0 0 8 12"><path d="M6 1L1.5 6L6 11" stroke="#fff" stroke-width="2" fill="none"/></svg></div>
<div class="arrow next"><svg width="8" height="12" viewBox="0 0 8 12"><path d="M2 1L6.5 6L2 11" stroke="#fff" stroke-width="2" fill="none"/></svg></div>
<div class="slider-shadow"></div>

<article class="card" style="left:172px">
  <h2>About Us</h2>
  <p>Crestline Forge Alloys is a national distributor specializing in the distribution of stainless steel, titanium, and aluminum bar stock, sheet, plate, pipe, tubing, wire, and coil. We have 7 stocking facilities throughout the country offering 1-2 day</p>
  <div class="read-more">Read More</div>
</article>
<article class="card" style="left:465px">
  <h2>Service is our business</h2>
  <h4>Large Volume Requirements</h4>
  <p>Have a large volume stainless requirement? We can most likely beat out anyone on price, quality, and service, whether you have pricing from a mill or another distributor.</p>
  <div class="read-more">Read More</div>
</article>
<article class="card" style="left:759px">
  <h2>Testimonials</h2>
  <p class="quote"><span class="mark open">“</span>Lorem ipsum dolor sit amet, consectetur adipiscing elit, sed do eiusmod tempor incididunt ut labore et dolore magna aliqua. Ut enim ad minim veniam, quis nostrud exercitation ullamco laboris nisi ut aliquip<span class="mark close">”</span></p>
  <div class="read-more">Read More</div>
</article>

<footer class="footer">
  <svg class="cert-seal" width="141" height="141" viewBox="0 0 141 141" role="img" aria-label="Quality certification seal">
    <circle cx="70.5" cy="70.5" r="69" fill="#fff"/>
    <circle cx="70.5" cy="70.5" r="64" fill="none" stroke="var(--blue)" stroke-width="4"/>
    <circle cx="70.5" cy="70.5" r="44" fill="var(--blue)"/>
  </svg>
  <div class="divider" style="left:378px"></div>
  <div class="info" style="left:405px">418 Harbor Mill Rd.<br>Millbrook, OH 44000</div>
  <div class="divider" style="left:575px"></div>
  <div class="info" style="left:611px">555-273-8640<br>sales@crestlineforgealloys.example</div>
  <div class="quote-btn">Request a Quote</div>
  <div class="rule"></div>
  <div class="copyright">©2014 Crestline Forge Alloys, All Rights Reserved.</div>
  <div class="social" style="left:901px"></div>
  <div class="social" style="left:935px"></div>
  <div class="social" style="left:969px"></div>
</footer>
</body>
</html>
```